New fresh design for ShopHarbor Golf website

GOLF ECOMMERCE - We have had a new logo designed which we are happy with and now want this new theme rolled out across our ShopHarbor store, Trovio Shop Template, Chatterly - Exciting modern, fresh design required with excellent menu presentation and ease of use the key priorities. Ongoing, I am looking for regular banner updates. I have attached our new logo designs so you can get a feel of the look.

Target Market(s)

UK Golfers

Industry/Entity Type

Store

Font styles to use
Sans Serif

Colors
0455a3
f37122
33a6d7
eaf1f7

Requirements
Must have
• Workable easy to read menu structure. Room for banners and Ratewell.co.uk widget. Social visibility icons

```html
<!DOCTYPE html>
<html lang="en">
<head>
<meta charset="utf-8">
<title>ParLane Golf</title>
<link rel="stylesheet" href="https://fonts.googleapis.com/css2?family=Roboto:wght@400;500;700&family=Oswald:wght@400;500&display=swap">
<style>
:root{
  --orange:#f37122;
  --nav:#7282dc;
  --blue:#4f5fc4;
  --ink:#333;
  --muted:#666;
  --topbar:#ececec;
  --page:#f2f2f2;
  --footer:#eceef6;
  --dark:#333333;
  --price:#e0341d;
}
*{box-sizing:border-box;margin:0;padding:0}
html,body{width:744px;height:1200px;overflow:hidden}
body{position:relative;background:var(--page);font-family:Roboto,sans-serif;color:var(--ink)}
.abs{position:absolute}
.topbar{left:0;top:0;width:744px;height:23px;background:var(--topbar);font-size:7.5px;color:#444}
.topbar .call{left:56px;top:9px}
.topbar .links{right:57px;top:7px}
.header{left:0;top:23px;width:744px;height:60px;background:#fff}
.logo{left:55px;top:18px;font-size:22px;font-weight:700;color:var(--blue);letter-spacing:.5px}
.search{left:490px;top:21px;width:153px;height:23px;border:1px solid #ccc;background:#fff}
.search span{position:absolute;left:7px;top:7px;font-size:6.5px;color:#999}
.search .btn{position:absolute;right:-1px;top:-1px;width:22px;height:23px;background:var(--nav)}
.cart{left:655px;top:20px;width:27px;height:27px;border-radius:50%;border:1px solid var(--orange);background:#fff}
.cart-count{left:671px;top:9px;width:16px;height:16px;border-radius:50%;border:1px solid #555;background:#fff;font-size:8px;text-align:center;line-height:14px}
.rule{left:0;top:83px;width:744px;height:3px;background:var(--orange)}
.nav{left:0;top:86px;width:744px;height:39px;background:var(--nav);display:flex;align-items:center;font-size:8.5px;color:#fff;text-transform:uppercase}
.nav .shop{position:absolute;left:55px;top:0;width:81px;height:39px;background:var(--orange);padding:16px 0 0 13px}
.nav ul{list-style:none;position:absolute;left:153px;top:15px;display:flex;gap:23px}
.hero{left:0;top:125px;width:744px;height:322px;background:linear-gradient(90deg,#6d9a3c,#a7c25a 50%,#5e8a32)}
.hero-photo{left:55px;top:125px;width:634px;height:322px;background:radial-gradient(ellipse at 60% 40%,#d5e3a6,#97b751 50%,#4f7a28)}
.hero h1{left:98px;top:198px;font-family:Oswald,sans-serif;font-weight:400;font-size:22px;color:#fff}
.hero .save{left:96px;top:230px;font-family:Oswald,sans-serif;font-weight:400;font-size:37px;color:#f7b21d;letter-spacing:1px}
.hero .sub{left:99px;top:285px;font-size:12px;color:#fff}
.arrow{top:403px;width:23px;height:29px;background:#222}
.promo{top:456px;width:314px;height:151px}
.promo h2{position:absolute;left:23px;top:34px;font-family:Oswald,sans-serif;font-weight:400;font-size:15px;color:#fff}
.promo h3{position:absolute;left:23px;top:54px;font-size:13px;font-weight:500}
.promo p{position:absolute;left:23px;top:75px;font-size:9px}
.promo .buy{position:absolute;left:24px;top:98px;width:63px;height:22px;background:var(--orange);color:#fff;font-size:9px;text-align:center;line-height:22px}
.section-title{left:58px;top:630px;font-size:12.5px;color:#333}
.section-title b{font-weight:400;color:var(--orange)}
.circ{top:629px;width:16px;height:16px;border-radius:50%;border:1.5px solid #222}
.card{top:656px;width:150px;height:195px;background:#fff;border:1px solid #ddd;box-shadow:0 1px 3px rgba(0,0,0,.15)}
.card .img{position:absolute;left:10px;top:7px;width:130px;height:140px;background:linear-gradient(#f4f4f4,#e4e4e4);border:1px solid #ddd}
.card .name{position:absolute;left:12px;top:158px;font-size:10px}
.card .price{position:absolute;left:12px;top:174px;font-size:8.5px;color:var(--price)}
.card .add{position:absolute;right:15px;top:158px;width:21px;height:21px;border-radius:50%;background:var(--orange)}
.brands-title{left:0;top:871px;width:744px;text-align:center;font-size:9.5px}
.brands{left:57px;top:888px;width:636px;height:83px;background:radial-gradient(ellipse at center,#fff 40%,#e0e0e0);display:flex;justify-content:space-around;align-items:center;font-size:12px;font-weight:700;color:#111}
.footer{left:0;top:990px;width:744px;height:153px;background:var(--footer)}
.fcol h4{font-size:11px;font-weight:400;color:var(--orange)}
.fcol p,.fcol li{font-size:8.5px;line-height:15px;color:#444;list-style:none}
.vline{top:1015px;width:1px;height:120px;background:#bbb}
.newsbox{left:387px;top:1054px;width:140px;height:21px;background:#fff;border:1px solid #bbb}
.pay{top:1101px;width:24px;height:16px;border-radius:2px}
.widget{left:561px;top:1016px;width:116px}
.thumbs{display:grid;grid-template-columns:repeat(4,25px);gap:3px;margin-top:8px}
.thumbs div{height:25px;background:#b9a79a}
.bottom{left:0;top:1143px;width:744px;height:57px;background:var(--dark)}
.bottom .copy{left:83px;top:24px;font-size:8.5px;color:#fff}
.social{top:1164px;width:20px;height:20px;border-radius:3px}
</style>
</head>
<body>
<div class="abs topbar">
  <span class="abs call">CALL US : 01632 960431</span>
  <span class="abs links">Sign in or Create an account &nbsp;|&nbsp; My Account &nbsp;|&nbsp; My Favorites</span>
</div>
<div class="abs header">
  <div class="abs logo">ParLane Golf</div>
  <div class="abs search"><span>SEARCH</span><div class="btn">
    <svg width="22" height="23" viewBox="0 0 22 23"><circle cx="10" cy="10.5" r="3.5" fill="none" stroke="#fff" stroke-width="1.4"/><line x1="12.5" y1="13" x2="15" y2="15.5" stroke="#fff" stroke-width="1.4"/></svg>
  </div></div>
  <div class="abs cart"><svg width="25" height="25" viewBox="0 0 25 25"><path d="M7 11h11l-1.5 6h-8z" fill="var(--orange)"/><path d="M9 11l3-4 3 4" fill="none" stroke="var(--orange)" stroke-width="1.3"/></svg></div>
  <div class="abs cart-count">0</div>
</div>
<div class="abs rule"></div>
<nav class="abs nav">
  <div class="shop">SHOP ALL &#9662;</div>
  <ul><li>Recycled Golf Balls</li><li>Special Offers</li><li>Golf Day Discounts</li><li>Cleats &amp; Spikes</li><li>Golf Tees</li><li>Golf Bags</li></ul>
</nav>
<section>
  <div class="abs hero" role="img" aria-label="Golf course fairway background"></div>
  <div class="abs hero-photo" role="img" aria-label="Gloved hand placing a golf ball on a tee beside an iron club"></div>
  <div class="hero">
    <h1 class="abs">ESSENTIAL ACCESORIES</h1>
    <div class="abs save">20% SAVE</div>
    <div class="abs sub">IPSUM IS SIMPLY DUMMY TEXT</div>
  </div>
  <div class="abs arrow" style="left:622px"><svg width="23" height="29"><path d="M14 8l-6 6.5 6 6.5" fill="none" stroke="#fff" stroke-width="1.3"/></svg></div>
  <div class="abs arrow" style="left:647px"><svg width="23" height="29"><path d="M9 8l6 6.5-6 6.5" fill="none" stroke="#fff" stroke-width="1.3"/></svg></div>
</section>
<div class="abs promo" style="left:56px;background:linear-gradient(100deg,#5f8e1f,#a7c641 60%,#d6e6a0)" role="img" aria-label="Golf ball on a tee on green grass">
  <h2>RECYCLED GOLF BALLS</h2><h3 style="color:#fff">STORE SPECIALS</h3><p style="color:#fff">Ipsum is simply dummy text</p><div class="buy">BUY NOW</div>
</div>
<div class="abs promo" style="left:374px;background:linear-gradient(100deg,#f0f0dc,#d9dfb4 55%,#8b9a5c)" role="img" aria-label="Golf bag full of clubs">
  <h2 style="color:#5565c8">GOLF DAY DISCOUNTS</h2><h3 style="color:#333">STORE SPECIALS</h3><p style="color:#777">Ipsum is simply dummy text</p><div class="buy">BUY NOW</div>
</div>
<div class="abs section-title">FEATURED <b>PRODUCTS</b></div>
<div class="abs circ" style="left:655px"><svg width="13" height="13"><path d="M7.5 3.5l-3 3 3 3" fill="none" stroke="#222" stroke-width="1.4"/></svg></div>
<div class="abs circ" style="left:673px"><svg width="13" height="13"><path d="M5.5 3.5l3 3-3 3" fill="none" stroke="#222" stroke-width="1.4"/></svg></div>
<div class="abs card" style="left:59px"><div class="img" role="img" aria-label="Golf cart bag"></div><div class="name">Product Name</div><div class="price">ONLY: $25</div><div class="add"></div></div>
<div class="abs card" style="left:220px"><div class="img" role="img" aria-label="Blue golf glove"></div><div class="name">Product Name</div><div class="price">ONLY: $25</div><div class="add"></div></div>
<div class="abs card" style="left:381px"><div class="img" role="img" aria-label="Golf training grip"></div><div class="name">Product Name</div><div class="price">ONLY: $25</div><div class="add"></div></div>
<div class="abs card" style="left:541px"><div class="img" role="img" aria-label="Novelty golf ball marker"></div><div class="name">Product Name</div><div class="price">ONLY: $25</div><div class="add"></div></div>
<div class="abs brands-title">POPULAR BRANDS</div>
<div class="abs brands"><span>Stonebridge</span><span>Kestrel</span><span>Strideline</span><span>Vantor</span><span>Hollisford</span><span>Birchwell</span></div>
<footer>
  <div class="abs footer"></div>
  <div class="abs fcol" style="left:78px;top:1014px;width:140px">
    <h4>CONTACT US</h4>
    <p style="margin-top:8px;padding-left:2px">Lorem Ipsum has been the standard dummy text ever since when an unknown printer<br>Tel 010-5550142<br>Email info@parlanegolf.example</p>
  </div>
  <div class="abs vline" style="left:224px"></div>
  <div class="abs fcol" style="left:249px;top:1014px">
    <h4>MY ACCOUNT</h4>
    <ul style="margin-top:8px;padding-left:5px"><li>Your Account</li><li>My orders</li><li>My credit slips</li><li>My addresses</li><li>Login</li></ul>
  </div>
  <div class="abs vline" style="left:362px"></div>
  <div class="abs fcol" style="left:385px;top:1014px">
    <h4>NEWSLETTER</h4>
    <p style="margin-top:8px;padding-left:2px">Sign Up for Our Newsletter:</p>
    <p style="margin-top:23px;padding-left:2px">Payment</p>
  </div>
  <div class="abs newsbox"><svg class="abs" style="right:4px;top:6px" width="6" height="8"><path d="M0 0l6 4-6 4z" fill="#333"/></svg></div>
  <div class="abs pay" style="left:388px;background:#f3e6c8"></div>
  <div class="abs pay" style="left:416px;background:#f5c84a"></div>
  <div class="abs pay" style="left:444px;background:#3d6ea8"></div>
  <div class="abs pay" style="left:472px;background:#d64a2e"></div>
  <div class="abs pay" style="left:500px;background:#2c4b8e"></div>
  <div class="abs vline" style="left:543px"></div>
  <div class="abs widget">
    <div style="font-size:13px;font-weight:700;color:var(--blue)">ParLane Golf</div>
    <div style="font-size:5.5px;color:#666;margin-top:5px;border-top:1px solid #ddd;padding-top:3px">32,742 people like <span style="color:var(--blue)">ParLane</span></div>
    <div class="thumbs" role="img" aria-label="Member avatars">
      <div></div><div style="background:#d8dce4"></div><div style="background:#cfc6b8"></div><div style="background:#6d5a4d"></div>
      <div style="background:#e8c58f"></div><div style="background:#b9a8c8"></div><div style="background:#d0a89a"></div><div style="background:#a33a2a"></div>
    </div>
    <div style="font-size:5px;color:#888;margin-top:4px;border-top:1px solid #ddd;padding-top:3px">&#9632; Chatterly social plugin</div>
  </div>
  <div class="abs bottom"><span class="abs copy">Copyright &copy; 2014 &nbsp;All rights reserved.</span></div>
  <div class="abs social" style="left:565px;background:#5fb6e0"></div>
  <div class="abs social" style="left:592px;background:#3f5f9c"></div>
  <div class="abs social" style="left:619px;background:#5fa9c8"></div>
  <div class="abs social" style="left:646px;background:#8a6f55"></div>
</footer>
</body>
</html>
```